New Business Card Design

we need a new business card as we have just moved location and need a fresh new look. we are a Land Surveying Company . the card needs to be 2 sided and needs to have what we do on the back as our previous card ( attached ).
i was thinking of maybe a ruler down the bottom of the card or something to make it stand out. size can be 90 x 55 or 90 x 45 .
maybe a shadow of the logo or something in the corner.
on the attached card where it says other offices , it should be Melbourne instead of bendigo

postal address should be there as PO box 812 , Thornbury Flats 3821
Updates

Reason: some designs didn't follow brief by having services provided on the back of the card, just giving a bit of time toi change and to review.

Industry/Entity Type

Business

Requirements
Must have
• All cards need to have services provided on the back please , as stated , a lot of designs have just had the logo on the back

```html
<!DOCTYPE html>
<html lang="en">
<head>
<meta charset="utf-8">
<title>Marlow Keating Land Surveyors – Business Card</title>
<link rel="stylesheet" href="https://fonts.googleapis.com/css2?family=Arimo:wght@400;700&display=swap">
<style>
  :root {
    --page-bg: #ececec;
    --panel-light: #e9eaec;
    --brand-blue: #0a66b8;
    --ring-faint: rgba(255,255,255,0.12);
    --ink: #111111;
    --ink-soft: #2a2a2a;
    --on-blue: #e8f0f8;
    --logo-grey: #7a7c80;
  }
  * { box-sizing: border-box; margin: 0; padding: 0; }
  html, body { width: 1200px; height: 1000px; overflow: hidden; }
  body {
    background: var(--page-bg);
    font-family: "Arimo", Arial, sans-serif;
    position: relative;
  }
  .card {
    position: absolute;
    left: 300px;
    width: 600px;
    height: 300px;
    display: flex;
    overflow: hidden;
  }
  .card--front { top: 150px; }
  .card--back { top: 540px; }
  .card__side {
    background: var(--panel-light);
    width: 204px;
    position: relative;
    padding: 36px 0 0 20px;
  }
  .card__main {
    flex: 1;
    background: var(--brand-blue);
    position: relative;
    color: var(--on-blue);
    box-shadow: inset 3px 0 4px rgba(0,0,0,0.18);
  }
  .card__watermark {
    position: absolute;
    left: 60px;
    top: 10px;
    width: 280px;
    height: 280px;
  }
  .brand {
    display: flex;
    align-items: center;
    gap: 8px;
  }
  .brand__dot {
    width: 30px; height: 30px;
    border-radius: 50%;
    border: 3px solid var(--logo-grey);
    flex: none;
  }
  .brand__name {
    font-size: 13px;
    font-weight: 700;
    color: var(--ink);
    line-height: 1.15;
    letter-spacing: 0.5px;
  }
  .person { position: absolute; left: 22px; top: 150px; }
  .person__name { font-size: 17px; color: var(--ink); margin-bottom: 6px; }
  .person__line { font-size: 13px; color: var(--ink-soft); line-height: 23.5px; }
  .contact {
    position: relative;
    padding: 36px 0 0 86px;
    font-size: 13px;
    line-height: 23.5px;
  }
  .contact__group + .contact__group { margin-top: 23px; }
  .contact__row { display: flex; }
  .contact__label { width: 80px; }
  .memberships {
    position: absolute;
    left: 22px; top: 130px;
    font-size: 13px;
    line-height: 22px;
    color: var(--ink);
  }
  .memberships__offices { margin-top: 22px; }
  .services {
    position: relative;
    list-style: none;
    padding: 34px 0 0 70px;
    font-size: 13px;
    line-height: 24px;
  }
  .services li { position: relative; padding-left: 18px; }
  .services li::before {
    content: "";
    position: absolute;
    left: 0; top: 9px;
    width: 6px; height: 6px;
    border-radius: 50%;
    background: var(--on-blue);
  }
  .services__sub { display: block; padding-left: 40px; }
</style>
</head>
<body>

<section class="card card--front" aria-label="Business card front">
  <div class="card__side">
    <div class="brand">
      <span class="brand__dot"></span>
      <span class="brand__name">MARLOW KEATING<br>LAND SURVEYORS</span>
    </div>
    <div class="person">
      <p class="person__name">Daniel Keating</p>
      <p class="person__line">B.App.Sci.(Surv) MIS(Aust)</p>
      <p class="person__line">Grad.Dip.(Surv Prac)</p>
      <p class="person__line">Licensed Surveyor</p>
      <p class="person__line">Director</p>
    </div>
  </div>
  <div class="card__main">
    <svg class="card__watermark" viewBox="0 0 280 280" aria-hidden="true">
      <circle cx="140" cy="140" r="124" fill="none" stroke="var(--ring-faint)" stroke-width="22"/>
    </svg>
    <div class="contact">
      <div class="contact__group">
        <p>Cnr Ashby Court and Linton Street,</p>
        <p>Ridgeview East 3694</p>
        <p>PO box 812 , Thornbury Flats 3821</p>
      </div>
      <div class="contact__group">
        <p class="contact__row"><span class="contact__label">telephone:</span>03 5550 2146</p>
        <p class="contact__row"><span class="contact__label">facsimile:</span>03 5550 2147</p>
        <p class="contact__row"><span class="contact__label">mobile:</span>0400 555 318</p>
      </div>
      <div class="contact__group">
        <p class="contact__row"><span class="contact__label">email:</span>daniel@marlowkeating.com.au</p>
        <p class="contact__row"><span class="contact__label">website:</span>marlowkeating.com.au</p>
      </div>
    </div>
  </div>
</section>

<section class="card card--back" aria-label="Business card back">
  <div class="card__side">
    <div class="brand">
      <span class="brand__dot"></span>
      <span class="brand__name">MARLOW KEATING<br>LAND SURVEYORS</span>
    </div>
    <div class="memberships">
      <p>Member of Survey</p>
      <p>Practitioners Guild</p>
      <p>Member of Regional</p>
      <p>Land Development</p>
      <p>Council</p>
      <p class="memberships__offices">Other Offices: Westhaven</p>
    </div>
  </div>
  <div class="card__main">
    <svg class="card__watermark" viewBox="0 0 280 280" aria-hidden="true">
      <circle cx="140" cy="140" r="124" fill="none" stroke="var(--ring-faint)" stroke-width="22"/>
    </svg>
    <ul class="services">
      <li>Subdivisions</li>
      <li>Check Title Boundaries</li>
      <li>Features &amp; Level Surveys</li>
      <li>Neighborhood &amp; Site Description Plans<span class="services__sub">for Development Permits</span></li>
      <li>Town Planning / Estate Designs</li>
      <li>Civil Engineering Surveys<span class="services__sub">(Roads, Structural &amp; Earthworks)</span></li>
    </ul>
  </div>
</section>

</body>
</html>
```